Basic Letterhead Design

We need a Letterhead design. Our company is in the financial services industry. We are a small bank who lends money. I have uploaded an example our current letterhead design. We would like a new one.

```html
<!DOCTYPE html>
<html lang="en">
<head>
<meta charset="utf-8">
<title>Larkfield Capital Letterhead</title>
<link href="https://fonts.googleapis.com/css2?family=Tinos:wght@400;700&display=swap" rel="stylesheet">
<style>
  :root {
    --backdrop: #e8e8e9;
    --paper: #ffffff;
    --brand-green: #244c37;
    --band-grey: #4a4946;
    --ink: #2b2b2b;
    --signature-tone: #e4e4e2;
  }
  * { margin: 0; padding: 0; box-sizing: border-box; }
  html, body {
    width: 1200px; height: 874px; overflow: hidden;
    background: var(--backdrop);
    font-family: "Tinos", "Times New Roman", serif;
    color: var(--ink);
  }
  .letterhead {
    position: absolute; left: 310px; top: 27px;
    width: 580px; height: 820px;
    background: var(--paper);
    box-shadow: 0 2px 10px rgba(0,0,0,0.12);
    overflow: hidden;
  }
  .brand {
    position: absolute; left: 48px; top: 92px;
    display: flex; align-items: center; gap: 10px;
  }
  .brand-dot { width: 18px; height: 18px; background: var(--brand-green); border-radius: 50%; }
  .brand-name {
    font-size: 21px; font-weight: 400; letter-spacing: 2px;
    text-transform: uppercase; color: var(--brand-green);
  }
  .sender {
    position: absolute; right: 48px; top: 58px;
    padding-left: 14px; border-left: 1.5px solid var(--brand-green);
    font-size: 11.5px; line-height: 1.3;
  }
  .sender-name { color: var(--brand-green); font-weight: 700; font-size: 12.5px; }
  .letter-body {
    position: absolute; left: 48px; top: 200px; width: 480px;
    font-size: 12.5px; line-height: 1.75;
  }
  .classification { font-weight: 700; letter-spacing: 0.3px; }
  .offer-heading { font-weight: 700; margin-top: 18px; }
  .offer-terms { list-style: none; }
  .offer-terms li { position: relative; padding-left: 14px; }
  .offer-terms li::before { content: "•"; position: absolute; left: 0; }
  .closing { margin-top: 18px; }
  .signature {
    width: 130px; height: 46px; margin-top: 8px;
    background: var(--signature-tone); border-radius: 4px;
  }
  .footer-band { position: absolute; left: 0; bottom: 0; width: 580px; height: 70px; }
  .acn-text { font-family: "Tinos", "Times New Roman", serif; font-weight: 700; font-size: 15px; fill: #ffffff; }
</style>
</head>
<body>
  <main class="letterhead">
    <header>
      <div class="brand">
        <span class="brand-dot"></span>
        <span class="brand-name">Larkfield Capital</span>
      </div>
      <address class="sender" style="font-style: normal;">
        <div class="sender-name">Owen Pritchard</div>
        <div>Director</div>
        <div>Larkfield Capital Pty Ltd</div>
        <div>14 WATTLE GROVE</div>
        <div>MARLOW NSW 2299</div>
      </address>
    </header>

    <section class="letter-body">
      <p class="classification">COMMERCIAL-IN-CONFIDENCE</p>
      <p>Wednesday 23rd Feb 2022</p>
      <p>Att: Daniel Hartley, Harbourline Realty Rose Bay</p>
      <p>PROPOSED ACQUISITION: 14 Wattle Grove, Marlow NSW 2299</p>
      <p>The purpose of this letter is to provide an in-principle summary of our proposal between the Landowner (‘the Landowner’) and Larkfield Capital Pty Ltd (‘Larkfield’) to the terms of Sale of Lot 7 DP 418236 located at the aforementioned address.</p>
      <p class="offer-heading">Our offer is in two optional parts, as follows:</p>
      <ul class="offer-terms">
        <li>Purchase Price: $1,600,000</li>
        <li>Terms: 12-month Call Option + 4-month extension</li>
        <li>Deposit: 1% Option fee released upon exchange for 12 months. Plus 1% for a further 4 months if extended. (Total 2%)</li>
      </ul>
      <p class="closing">We look forward to hearing from you.</p>
      <p>Best Regards,</p>
      <div class="signature" role="img" aria-label="Handwritten signature of the director"></div>
    </section>

    <svg class="footer-band" viewBox="0 0 580 70" aria-hidden="false" role="img" aria-label="Footer band with company number">
      <polygon points="0,52 370,52 362,70 0,70" fill="var(--band-grey)"/>
      <polygon points="392,22 540,22 528,70 380,70" fill="var(--brand-green)"/>
      <text class="acn-text" x="458" y="51" text-anchor="middle">ACN: 512 088 317</text>
      <polygon points="556,22 580,22 580,42 551,42" fill="var(--band-grey)"/>
    </svg>
  </main>
</body>
</html>
```